Corporate Brochure for Exclusive Consultant Firm

Brochure needed for insurance adjusting firm. Our company is highly specialized in our field. Our target market are executives at insurance companies, insurance risk managers and insurance brokers. We specialize in industrial insurance claims in the mining, forestry, chemical plants, construction and legal liability sectors.

We are looking for a 8 1/2 x 11 bi-fold brochure that tells the story of our company. Our corporate colors are used. There is a place at the back for the pictures and short bios of the 3 people on our web site.

Refer to our web site for full details on our company. Please do not do cut and paste, we are looking for a creative, clean, professional design.

We want a brochure that we can send to the printer, so the necessary files for that. Also, we want the brochure to be in electronic form so we can distribute the brochure electronically.

www.halvorenclaims.example

Target Market(s)

Corporate executives

Industry/Entity Type

Insurance

Requirements
Must have
• clean, professional, modern look reflecting our website. Pictures of the 3 persons, short bio of each near the back. Can use photos from the site or use other files. Must provide files for print, and produce a digital version that we can share with clients electronically.
Nice to have
• COLORS: orange, light grey, white, black (to be used minimally, more as accent)
Should not have
• exact cut and paste from our website. We are looking for a clean modern and new brochure to market our business .

```html
<!DOCTYPE html>
<html lang="en">
<head>
<meta charset="utf-8">
<title>Halvoren Claims – Bi-fold Brochure</title>
<link href="https://fonts.googleapis.com/css2?family=Open+Sans:wght@400;600;700;800&display=swap" rel="stylesheet">
<style>
  :root{
    --orange:#f07c1b;
    --ink:#262626;
    --grey:#d8d9db;
    --mist:#eeeff0;
    --paper:#ffffff;
    --text:#555a60;
    --rule:#e2e3e5;
  }
  *{box-sizing:border-box;margin:0;padding:0}
  html,body{width:835px;height:1200px;overflow:hidden;background:var(--mist);font-family:"Open Sans",Arial,sans-serif;color:var(--text)}
  .canvas{position:relative;width:835px;height:1200px}
  .spread{position:absolute;left:45px;width:745px;background:var(--paper);box-shadow:0 2px 8px rgba(0,0,0,.18);overflow:hidden}
  .spread--outside{top:10px;height:540px}
  .spread--inside{top:575px;height:615px}
  .page{position:absolute;top:0;height:100%}
  .page--left{left:0;width:372px}
  .page--right{left:372px;width:373px}
  .fill{position:absolute}
  p{font-size:6.4px;line-height:1.55}

  /* bios */
  .bio{position:absolute;left:14px;width:346px;height:146px}
  .bio__photo{left:0;top:0;width:62px;height:82px;background:linear-gradient(160deg,#cfd2d6,#7d838a)}
  .bio__col{position:absolute;top:0;width:125px}
  .bio__col--a{left:74px}
  .bio__col--b{left:214px;width:132px}
  .bio__contact{margin-top:6px;color:var(--ink)}
  .contact-bar{position:absolute;left:0;bottom:0;width:100%;height:44px;background:var(--ink);text-align:center;padding-top:9px}
  .brand{font-weight:800;letter-spacing:.6px;text-transform:uppercase;color:var(--orange);display:inline-flex;align-items:center;gap:5px}
  .brand__dot{display:inline-block;background:var(--orange)}
  .contact-bar .brand{font-size:9px}
  .contact-bar .brand__dot{width:8px;height:8px}
  .contact-bar p{color:#bfc1c4;margin-top:3px;font-size:5.4px}

  /* cover */
  .cover-grid{left:0;top:0;width:100%;height:150px;background:linear-gradient(135deg,#5a5f66,#2e3135 60%,#8a8f95)}
  .cover-brand{position:absolute;left:0;top:150px;width:100%;height:42px;text-align:right;padding:12px 20px 0 0}
  .cover-brand .brand{font-size:16px}
  .cover-brand .brand__dot{width:14px;height:14px}
  .cover-photo{left:0;top:192px;width:100%;height:190px;background:linear-gradient(120deg,#b9bdc2,#6d7379 55%,#3b3f44)}
  .cover-copy{position:absolute;right:16px;top:392px;width:230px}
  .cover-copy h2{font-size:7.4px;font-weight:800;color:var(--ink);text-transform:uppercase;margin-bottom:5px;line-height:1.3}
  .web-bar{position:absolute;left:0;bottom:16px;width:100%;height:16px;background:var(--orange);color:#fff;font-size:6.4px;font-weight:700;text-align:right;padding:3px 16px 0 0}

  /* inside */
  .inside-photo{left:6px;top:6px;width:112px;height:603px;background:linear-gradient(180deg,#c9d3dc,#8394a4 40%,#4a5866)}
  .approach{position:absolute;left:128px;top:14px;width:232px}
  .approach h3,.sectors h3{color:var(--orange);font-weight:700}
  .approach h3{font-size:7.8px;margin:12px 0 3px}
  .approach h3:first-child{margin-top:0}
  .approach p{font-size:6.8px;line-height:1.6}
  .intro{position:absolute;left:22px;top:16px;width:330px}
  .intro p,.closing p{font-size:6.8px;line-height:1.6}
  .sectors{position:absolute;left:22px;top:62px;width:330px}
  .sectors h3{font-size:11.5px;padding:5px 0;border-bottom:1px solid var(--rule)}
  .closing{position:absolute;left:22px;top:250px;width:330px}
  .hex-photos{left:22px;top:322px;width:330px;height:280px;background:linear-gradient(135deg,#e9ecef,#9aa2ab 50%,#f3a25a)}
</style>
</head>
<body>
<div class="canvas">

  <section class="spread spread--outside">
    <div class="page page--left">
      <div class="bio" style="top:16px">
        <div class="fill bio__photo" role="img" aria-label="Portrait of Dana Whitlock"></div>
        <div class="bio__col bio__col--a"><p>Dana Whitlock is the founding partner and brings over twenty years of industrial claims handling across energy, chemical and heavy industry. Dana has led complex losses from first notice through to final settlement, working with carriers, brokers and risk managers on some of the largest files in the region.</p></div>
        <div class="bio__col bio__col--b"><p>A licensed adjuster in several provinces, Dana holds a designation as a Chartered Insurance Professional and is an active member of the national adjusters association.</p>
          <p class="bio__contact">dana@halvorenclaims.example<br>T 555 014 2201<br>C 555 014 2290</p></div>
      </div>
      <div class="bio" style="top:170px">
        <div class="fill bio__photo" role="img" aria-label="Portrait of Colin Marsh"></div>
        <div class="bio__col bio__col--a"><p>Colin Marsh is a senior adjuster with an engineering degree and many years of plant operations experience. He focuses on machinery breakdown, boiler and large property losses, bringing a technical eye to the cause and scope of every claim he manages.</p></div>
        <div class="bio__col bio__col--b"><p>Colin works closely with insurers, brokers and risk managers to scope damage, review business interruption and deliver clear, timely reporting.</p>
          <p class="bio__contact">colin@halvorenclaims.example<br>T 555 014 2202<br>C 555 014 2291</p></div>
      </div>
      <div class="bio" style="top:324px">
        <div class="fill bio__photo" role="img" aria-label="Portrait of Jared Pell"></div>
        <div class="bio__col bio__col--a"><p>Jared Pell joined the firm after a decade in forestry and mining claims, handling property, liability and construction files across remote operations. He is known for practical site work and careful documentation on demanding assignments.</p></div>
        <div class="bio__col bio__col--b"><p>Jared supports counsel and carriers through litigation when files require it, and holds a professional adjusting licence.</p>
          <p class="bio__contact">jared@halvorenclaims.example<br>T 555 014 2203<br>C 555 014 2292</p></div>
      </div>
      <div class="contact-bar">
        <span class="brand"><span class="brand__dot"></span>Halvoren Claims</span>
        <p>Suite 400, 120 Ridgeway Avenue, Northfield &nbsp;|&nbsp; T 555 014 2200 &nbsp;|&nbsp; www.halvorenclaims.example</p>
      </div>
    </div>

    <div class="page page--right">
      <div class="fill cover-grid" role="img" aria-label="Industrial plant photo collage in grey tones"></div>
      <div class="cover-brand"><span class="brand"><span class="brand__dot"></span>Halvoren Claims</span></div>
      <div class="fill cover-photo" role="img" aria-label="Photo of industrial pipework"></div>
      <div class="cover-copy">
        <h2>Technical expertise for specialty insurance markets</h2>
        <p>Halvoren Claims is a firm of highly skilled claims adjusters and loss management professionals. We specialize in managing and settling large, complex losses in the energy, chemical, forestry, mining and commercial sectors, giving our clients accurate answers, dependable reporting and complete technical support for every file we handle.</p>
      </div>
      <div class="web-bar">www.halvorenclaims.example</div>
    </div>
  </section>

  <section class="spread spread--inside">
    <div class="page page--left">
      <div class="fill inside-photo" role="img" aria-label="Photo of modern office towers against the sky"></div>
      <div class="approach">
        <h3>Our Approach</h3>
        <p>Our unique adjusting approach is rooted in engineering thinking and an accountable, hands-on presence at every loss site, from the first call to the final report.</p>
        <h3>Experience</h3>
        <p>Proven industry experience, a deep network of experts and a dedicated team that knows each sector, so clients understand the facts of every claim quickly and clearly.</p>
        <h3>The Difference</h3>
        <p>We work as a natural extension of our clients' own teams, bringing senior people to each file and keeping communication open from start to finish.</p>
        <h3>Niche Expertise</h3>
        <p>Our adjusters focus on specialty and heavy industrial risks, with practical knowledge of process plants, mills, mines and major construction projects.</p>
        <h3>Loss Control</h3>
        <p>Early site attendance, careful scoping and firm cost control help limit the severity of losses and support a fair, well documented outcome for all parties.</p>
        <h3>Customer Service Tailored to Your Needs</h3>
        <p>We align with the reporting standards of each carrier and broker, adapting our service to meet expectations for format, timing and level of detail.</p>
        <h3>Extensive Experience</h3>
        <p>Our team has handled a wide range of complex losses across many regions, giving insurers and risk managers confidence that their claims are in capable hands.</p>
      </div>
    </div>
    <div class="page page--right">
      <div class="intro"><p>Whether complex industrial property or liability claims, our adjusters provide a tailored claims management service in the following sectors:</p></div>
      <div class="sectors">
        <h3>Energy</h3>
        <h3>Chemical Operations</h3>
        <h3>Forest Industry</h3>
        <h3>Mining</h3>
        <h3>Commercial Claims</h3>
        <h3>Litigation Support Services</h3>
      </div>
      <div class="closing"><p>We are dedicated to quality, prompt reporting and clients with a personal, service-first approach to claims handling. Experience, sector knowledge and the judgement to manage every stage of a loss help us give insurers the best result on each assignment.</p></div>
      <div class="fill hex-photos" role="img" aria-label="Cluster of hexagonal photos of industrial and forestry sites"></div>
    </div>
  </section>

</div>
</body>
</html>
```